New Packaging Design Project

Wine packaging redesign. Retail partner requested a redesign of a private label wine. The old label is attached. Our partner liked the Lantern and Briar label and wanted something similar. There will be a logo added to the top of the label

Went on vacation/holiday

```html
<!DOCTYPE html>
<html lang="en">
<head>
<meta charset="utf-8">
<title>Napa Valley Red Blend – Label Pair</title>
<link rel="stylesheet" href="https://fonts.googleapis.com/css2?family=Anton&family=Montserrat:wght@400&family=Cormorant+Garamond:wght@500&family=Cinzel:wght@400&display=swap">
<style>
  :root {
    --page: #ffffff;
    --light-label: #ececea;
    --light-ink: #111111;
    --light-grey: #6f6f6f;
    --navy: #1f2a3a;
    --gold: #b98a55;
    --dark-label: #121212;
    --dark-ink: #d9d6cf;
    --dark-grey: #d8d8d8;
    --texture-dark: #3a3a3a;
    --texture-light: #9c9a92;
  }
  * { margin: 0; padding: 0; box-sizing: border-box; }
  html, body { width: 965px; height: 1200px; overflow: hidden; background: var(--page); }
  .canvas {
    width: 965px; height: 1200px;
    display: flex; align-items: center; justify-content: center; gap: 45px;
  }
  .label {
    position: relative; width: 430px; height: 468px; overflow: hidden;
  }
  .label--light { background: var(--light-label); color: var(--light-ink); }
  .label--dark { background: var(--dark-label); color: var(--dark-ink); }
  .label__art {
    position: absolute; left: 0; top: 185px; width: 430px; height: 283px;
  }
  .label__title {
    position: absolute; top: 48px; left: 0; width: 100%;
    text-align: center;
    font-family: "Anton", sans-serif;
    font-size: 60px; line-height: 1; letter-spacing: 0.5px;
    transform: scaleX(0.82);
  }
  .label__varietals {
    position: absolute; top: 125px; left: 0; width: 100%;
    text-align: center;
    font-family: "Montserrat", sans-serif;
    font-size: 10px; line-height: 16px; letter-spacing: 0.4px;
    text-transform: uppercase;
  }
  .label--light .label__varietals { color: var(--light-grey); }
  .label--dark .label__varietals { color: var(--dark-grey); }
  .label__vintage {
    position: absolute; top: 156px; right: 50px;
    font-family: "Cormorant Garamond", serif;
    font-size: 30px; letter-spacing: 3px; color: var(--gold);
  }
  .label__style {
    position: absolute; top: 248px; left: 18px;
    font-family: "Cinzel", serif;
    font-size: 20px; letter-spacing: 3px;
  }
  .label--light .label__style { color: var(--navy); }
  .label--dark .label__style { color: var(--dark-grey); }
</style>
</head>
<body>
<main class="canvas">

  <section class="label label--light">
    <svg class="label__art" viewBox="0 0 430 283" role="img" aria-label="Stippled mountain range above a speckled dark hillside">
      <defs>
        <linearGradient id="hills-light" x1="0" y1="0" x2="0" y2="1">
          <stop offset="0" stop-color="#ececea"/>
          <stop offset="0.4" stop-color="#c9c9c6"/>
          <stop offset="0.7" stop-color="#5a5a5a"/>
          <stop offset="1" stop-color="#3a3a3a"/>
        </linearGradient>
      </defs>
      <rect width="430" height="283" fill="url(#hills-light)"/>
    </svg>
    <h1 class="label__title">Napa Valley</h1>
    <p class="label__varietals">Merlot / Cabernet / Sauvignon/<br>Cabernet Franc / Petiti Verdot / Malbec</p>
    <p class="label__vintage">2018</p>
    <p class="label__style">Red Blend</p>
  </section>

  <section class="label label--dark">
    <svg class="label__art" viewBox="0 0 430 283" role="img" aria-label="Stippled mountain range above a speckled light hillside">
      <defs>
        <linearGradient id="hills-dark" x1="0" y1="0" x2="0" y2="1">
          <stop offset="0" stop-color="#121212"/>
          <stop offset="0.4" stop-color="#2e2e2e"/>
          <stop offset="0.7" stop-color="#8a8880"/>
          <stop offset="1" stop-color="#9c9a92"/>
        </linearGradient>
      </defs>
      <rect width="430" height="283" fill="url(#hills-dark)"/>
    </svg>
    <h1 class="label__title">Napa Valley</h1>
    <p class="label__varietals">Merlot / Cabernet / Sauvignon/<br>Cabernet Franc / Petiti Verdot / Malbec</p>
    <p class="label__vintage">2018</p>
    <p class="label__style">Red Blend</p>
  </section>

</main>
</body>
</html>
```